Horticulture Consulting Company Premium Card

We are looking for new design for a premium business card.
Our cards will be printed on glossy and embossed premium card stock.

Target Market(s)

Horticulture business owners needing our consulting services

Contact Information for Business Card

Marcus Thorne
(555) 348-2916
Marcus@velturaq.com

Requirements
Must have
• Company Logo and Contact information.
• Some additional work to add interest to the card
Should not have
• Red or Yellow

```html
<!DOCTYPE html>
<html lang="en">
<head>
<meta charset="utf-8">
<title>Velturaq Solutions — Business Card</title>
<link href="https://fonts.googleapis.com/css2?family=Lato:wght@400;700;900&display=swap" rel="stylesheet">
<style>
  :root {
    --backdrop: #2b2b2d;
    --card: #1f1f20;
    --card-edge: #2a2a2b;
    --green: #3bb54a;
    --blue: #1f7fd0;
    --white: #f2f2f2;
    --emboss: #8d8d90;
  }
  * { box-sizing: border-box; margin: 0; padding: 0; }
  html, body {
    width: 1200px; height: 900px; overflow: hidden;
    background: var(--backdrop);
    font-family: "Lato", sans-serif;
  }
  .stage {
    position: relative; width: 1200px; height: 900px;
    display: flex; flex-direction: column; align-items: center; justify-content: center; gap: 40px;
  }
  .card {
    position: relative; width: 700px; height: 400px;
    background: var(--card);
    border: 1px solid var(--card-edge);
    box-shadow: 0 14px 30px rgba(0,0,0,.45);
  }
  .card--front { display: flex; align-items: center; justify-content: center; }
  .brand { display: flex; align-items: center; gap: 18px; }
  .brand__dot { width: 46px; height: 46px; border-radius: 50%; flex: none; }
  .brand__name { font-weight: 900; font-size: 44px; letter-spacing: 1px; text-transform: uppercase; line-height: 1.1; }
  .card--front .brand__dot { background: #2c2c2e; box-shadow: inset 1px 1px 2px rgba(255,255,255,.08), inset -2px -2px 3px rgba(0,0,0,.6); }
  .card--front .brand__name { color: var(--emboss); }

  .card--back .brand {
    position: absolute; right: 50px; top: 95px; width: 240px;
    flex-direction: column; gap: 14px; text-align: center;
  }
  .card--back .brand__dot { width: 78px; height: 78px; background: var(--blue); }
  .card--back .brand__name { color: var(--green); font-size: 34px; }
  .brand__line { display: block; }

  .contact { position: absolute; left: 60px; top: 190px; color: var(--white); }
  .contact__name { color: var(--green); font-size: 34px; font-weight: 700; letter-spacing: 1px; text-transform: uppercase; line-height: 1; white-space: nowrap; }
  .contact__role { font-size: 19px; letter-spacing: 1px; margin: 6px 0 18px; }
  .contact__list { list-style: none; font-size: 21px; letter-spacing: .5px; }
  .contact__item { display: flex; align-items: center; gap: 10px; line-height: 30px; white-space: nowrap; }
  .contact__icon { width: 22px; height: 22px; flex: none; }
  .contact__accent { color: var(--green); }
</style>
</head>
<body>
<main class="stage">
  <section class="card card--front" aria-label="Card front">
    <div class="brand">
      <span class="brand__dot"></span>
      <span class="brand__name">Velturaq Solutions</span>
    </div>
  </section>

  <section class="card card--back" aria-label="Card back">
    <div class="contact">
      <h1 class="contact__name">Marcus Thorne</h1>
      <p class="contact__role">Owner</p>
      <ul class="contact__list">
        <li class="contact__item">
          <svg class="contact__icon" viewBox="0 0 22 22"><rect width="22" height="22" rx="4" fill="#1f7fd0"/><rect x="7" y="4" width="8" height="14" rx="1.5" fill="none" stroke="#fff" stroke-width="1.6"/><rect x="8.5" y="6" width="5" height="7" fill="#fff"/></svg>
          (555) 348-2916
        </li>
        <li class="contact__item">
          <svg class="contact__icon" viewBox="0 0 22 22"><rect width="22" height="22" rx="4" fill="#1f7fd0"/><rect x="4" y="6" width="14" height="10" rx="1" fill="#fff"/><path d="M4 6l7 6 7-6" fill="none" stroke="#1f7fd0" stroke-width="1.4"/></svg>
          Marcus@velturaq.com
        </li>
        <li class="contact__item">
          <svg class="contact__icon" viewBox="0 0 22 22"><rect width="22" height="22" rx="4" fill="#1f7fd0"/><g fill="none" stroke="#fff" stroke-width="1.3"><circle cx="11" cy="11" r="6.5"/><ellipse cx="11" cy="11" rx="3" ry="6.5"/><path d="M4.5 11h13M5.5 8h11M5.5 14h11"/></g></svg>
          <span>www.<span class="contact__accent">velturaq</span>.com</span>
        </li>
      </ul>
    </div>
    <div class="brand">
      <span class="brand__dot"></span>
      <span class="brand__name"><span class="brand__line">Velturaq</span><span class="brand__line">Solutions</span></span>
    </div>
  </section>
</main>
</body>
</html>
```